Update of Personal Website: geraldwinthorpe.com

This is a revamp of a personal website that already exists. Please visit the URL in the project title to view the current site.

An entirely fresh look is needed for the new site. Edits need to be made to the text included on the current site and photos must be added and subtracted. I will provide this.

Once a designer is selected, details about the necessities of the project will be discussed.

Target Market(s)

Business professionals

Industry/Entity Type

Real Estate Development

Coding

Coded - Design and coding required

Number of Pages Required

5+ page

Font styles to use
Sans Serif

Colors

Designer to choose colors to be used in the design.

Requirements
Must have
• Clean home page. Light background. Simplistic nature.
• Pages: Home, Family, Community, Business
Nice to have
• See attached images for examples of attractive sites.

```html
<!DOCTYPE html>
<html lang="en">
<head>
<meta charset="utf-8">
<title>Gerald Winthorpe — Real Estate Development</title>
<link href="https://fonts.googleapis.com/css2?family=Pathway+Gothic+One&family=Lato:ital,wght@0,300;0,400;1,400&display=swap" rel="stylesheet">
<style>
:root{
  --ink:#1d1d1d;
  --teal:#8cc7c9;
  --grey:#8a8a8a;
  --muted:#9a9a9a;
  --line:#e6e6e6;
  --hero-bg:#f6f6f6;
  --footer-bg:#f3f3f3;
  --bottom-bg:#121212;
  --white:#ffffff;
}
*{margin:0;padding:0;box-sizing:border-box}
html,body{width:830px;height:1200px;overflow:hidden;background:var(--white)}
body{position:relative;font-family:'Lato',sans-serif;color:var(--ink)}
.abs{position:absolute}
.display{font-family:'Pathway Gothic One',sans-serif;font-weight:400;text-transform:uppercase}

/* top nav */
.top-nav{left:0;top:0;width:830px;height:51px;background:var(--white);box-shadow:0 1px 3px rgba(0,0,0,.04);z-index:2}
.top-nav a{position:absolute;top:22px;font-size:10px;color:var(--muted);text-decoration:none;letter-spacing:.2px}
.top-nav a.active{color:var(--ink)}
.social-sq{position:absolute;top:18px;width:16px;height:16px;border-radius:2px}

/* hero */
.hero{left:0;top:51px;width:830px;height:365px;background:linear-gradient(180deg,#fbfbfb,var(--hero-bg))}
.hero-photo{left:395px;top:0;width:435px;height:365px;background:radial-gradient(ellipse at 55% 45%,#9d9d9d 0%,#5a5a5a 45%,#cfcfcf 80%,var(--hero-bg) 100%)}
.hero-name{left:64px;top:76px;font-size:96px;line-height:88px;color:var(--ink);letter-spacing:1px}
.hero-tag{left:65px;top:254px;font-size:33px;line-height:34px;color:var(--grey);letter-spacing:.5px}
.dots{left:393px;top:325px;display:flex;gap:7px}
.dots span{width:10px;height:10px;border-radius:50%;border:2px solid var(--white)}
.dots span.on{background:var(--teal);border-color:var(--teal)}

/* section heading */
.h-section{font-size:24px;line-height:26px;letter-spacing:.3px}
.h-section .accent{color:var(--teal)}
.rule{left:66px;top:454px;width:28px;height:2px;background:var(--ink)}

.about-intro{left:66px;top:514px;width:440px;font-size:11.2px;font-style:italic;line-height:19.5px;color:var(--ink)}
.about-body{left:66px;top:567px;width:440px;font-size:10.6px;line-height:19.5px;color:var(--grey);font-weight:400}
.btn{width:93px;height:26px;border:1px solid var(--ink);font-size:8.5px;display:flex;align-items:center;justify-content:center;letter-spacing:.3px;color:var(--ink);background:var(--white)}

/* cards */
.card{left:560px;width:202px;height:82px;border:1px solid var(--teal);background:var(--white)}
.card-photo{left:523px;width:87px;height:87px;border-radius:50%;border:2px solid var(--teal);padding:3px;background:var(--white)}
.card-photo i{display:block;width:100%;height:100%;border-radius:50%;background:linear-gradient(135deg,#6b6b6b,#2d2d2d)}
.card-title{left:618px;font-family:'Pathway Gothic One',sans-serif;font-size:19px;color:var(--ink)}
.card-desc{left:619px;width:135px;font-size:9.6px;line-height:13px;color:var(--grey)}

.divider{left:66px;top:776px;width:697px;height:1px;background:var(--line)}

/* news */
.news-date{left:66px;width:30px;height:31px;border:1px solid var(--ink);text-align:center}
.news-date b{display:block;font-weight:400;font-size:13px;line-height:14px;margin-top:5px}
.news-date small{display:block;font-size:6.5px;color:var(--grey);line-height:7px}
.news-title{left:107px;font-size:9.6px;color:var(--ink)}
.news-text{left:107px;width:180px;font-size:9.4px;line-height:12px;color:var(--grey)}

.blog-img{top:867px;width:129px;height:130px}

/* footer */
.footer-nav{left:0;top:1110px;width:830px;height:52px;background:var(--footer-bg)}
.footer-nav a{position:absolute;top:21px;font-size:10px;color:var(--ink);text-decoration:none}
.foot-circle{position:absolute;top:14px;width:19px;height:19px;border-radius:50%;border:1px solid #c8c8c8}
.bottom-bar{left:0;top:1162px;width:830px;height:38px;background:var(--bottom-bg);color:#cfcfcf;font-size:12.5px;font-weight:300;padding:11px 0 0 66px}
</style>
</head>
<body>

<nav class="abs top-nav">
  <a class="active" style="left:66px">HOME</a>
  <a style="left:146px">FAMILY</a>
  <a style="left:214px">COMMUNITY</a>
  <a style="left:304px">BUSINESS</a>
  <a style="left:395px">BLOG</a>
  <a style="left:460px">CONTACT US</a>
  <span class="social-sq" style="left:704px;background:#4a63a8" aria-label="Social link"></span>
  <span class="social-sq" style="left:726px;background:#3fa9e0" aria-label="Social link"></span>
  <span class="social-sq" style="left:748px;background:#3a8fc4" aria-label="Social link"></span>
</nav>

<header class="abs hero">
  <div class="abs hero-photo" role="img" aria-label="Black and white portrait of Gerald Winthorpe in a suit and tie"></div>
  <h1 class="abs display hero-name">Gerald<br>Winthorpe</h1>
  <p class="abs display hero-tag">Real Estate Development</p>
  <div class="abs dots"><span class="on"></span><span></span><span></span></div>
</header>

<section>
  <div class="abs rule"></div>
  <h2 class="abs display h-section" style="left:66px;top:472px"><span class="accent">About</span> Gerald Winthorpe</h2>
  <p class="abs about-intro">Gerald Winthorpe completed his first real estate transaction at the age of 19. He is now one of the most recognized contributors to the real estate industry in the Southern United States.</p>
  <p class="abs about-body">Winthorpe is the driving force behind the upscale residential and mixed-use communities of Winthorpe Development &amp; Realty LLC (WDR) and his most recent venture with Winthorpe-Halvorsen. Under his guidance, both brands set the standard for quality and consistency. While remaining committed to the centralized multifamily niche, his broad real estate portfolio includes office, institutional, recreational, and industrial applications.</p>
  <div class="abs btn" style="left:66px;top:687px">READ MORE</div>

  <div class="abs card" style="top:456px"></div>
  <div class="abs card-photo" style="top:454px" role="img" aria-label="Family portrait"><i></i></div>
  <div class="abs card-title" style="top:466px">Family</div>
  <div class="abs card-desc" style="top:498px">Devoted husband and father of five</div>

  <div class="abs card" style="top:552px"></div>
  <div class="abs card-photo" style="top:550px" role="img" aria-label="Portrait at a community event"><i></i></div>
  <div class="abs card-title" style="top:562px">Community</div>
  <div class="abs card-desc" style="top:594px">Devoted husband and father of five</div>

  <div class="abs card" style="top:649px"></div>
  <div class="abs card-photo" style="top:647px" role="img" aria-label="Business handshake in an office"><i></i></div>
  <div class="abs card-title" style="top:659px">Business</div>
  <div class="abs card-desc" style="top:691px">Devoted husband and father of five</div>
</section>

<div class="abs divider"></div>

<section>
  <h2 class="abs display h-section" style="left:66px;top:816px"><span class="accent">Latest</span> News</h2>

  <div class="abs news-date" style="top:867px"><b>01</b><small>Sept</small></div>
  <div class="abs news-title" style="top:866px">SAVE THE DATE!</div>
  <div class="abs news-text" style="top:881px">Contrary to popular belief, Lorem Ipsum is not simply random text.</div>

  <div class="abs news-date" style="top:915px"><b>01</b><small>Sept</small></div>
  <div class="abs news-title" style="top:913px">SAVE THE DATE!</div>
  <div class="abs news-text" style="top:928px">Contrary to popular belief, Lorem Ipsum is not simply random text.</div>

  <div class="abs news-date" style="top:961px"><b>01</b><small>Sept</small></div>
  <div class="abs news-title" style="top:960px">SAVE THE DATE!</div>
  <div class="abs news-text" style="top:975px">Contrary to popular belief, Lorem Ipsum is not simply random text.</div>

  <div class="abs btn" style="left:66px;top:1024px">READ MORE</div>
</section>

<section>
  <h2 class="abs display h-section" style="left:349px;top:816px"><span class="accent">Latest</span> Blogs</h2>
  <div class="abs blog-img" style="left:349px;background:linear-gradient(160deg,#8fb3d6,#4d6f96 55%,#2e3e54)" role="img" aria-label="Curved glass office tower against the sky"></div>
  <div class="abs blog-img" style="left:491px;background:linear-gradient(180deg,#3b6fb0,#3a3340 55%,#5a4a42)" role="img" aria-label="Hotel building at dusk with street traffic"></div>
  <div class="abs blog-img" style="left:633px;background:linear-gradient(120deg,#5c6f4e,#3a3f48 50%,#c9a23a)" role="img" aria-label="Engineer in a hard hat reviewing a site"></div>
  <div class="abs btn" style="left:349px;top:1024px">READ MORE</div>
</section>

<footer>
  <nav class="abs footer-nav">
    <a style="left:66px">HOME</a>
    <a style="left:142px">FAMILY</a>
    <a style="left:217px">COMMUNITY</a>
    <a style="left:320px">BUSINESS</a>
    <a style="left:415px">BLOG</a>
    <a style="left:481px">CONTACT US</a>
    <span class="foot-circle" style="left:695px"></span>
    <span class="foot-circle" style="left:720px"></span>
    <span class="foot-circle" style="left:744px"></span>
  </nav>
  <div class="abs bottom-bar">© Gerald Winthorpe 2017. All rights Reserved</div>
</footer>

</body>
</html>
```